construction co.logo(ie.highway,heavy equip)

need a design for a new construction company in washington state,office is located on the water (beach front)also use a 1952 halvorn dune vesper as portable office,or the standard bold construction type logo's,these are just thoughts and not necassarily direction

Target Market(s)

I will be working as a sub to much larger general contractors and am looking for a strong,stable appearance.

Industry/Entity Type

Construction

```html
<!DOCTYPE html>
<html lang="en">
<head>
<meta charset="utf-8">
<title>Saltwater General Contractors – Business Card</title>
<link rel="stylesheet" href="https://fonts.googleapis.com/css2?family=Cinzel:wght@600;700&family=Source+Sans+3:wght@400&display=swap">
<style>
  :root {
    --page-bg: #e9e9e9;
    --card-bg: #ffffff;
    --brand-blue: #1262e0;
    --brand-deep: #0b4fc4;
    --brand-light: #35c6f4;
    --rule-blue: #5a93e6;
  }
  * { margin: 0; padding: 0; box-sizing: border-box; }
  html, body { width: 1200px; height: 900px; overflow: hidden; }
  body {
    background: var(--page-bg);
    position: relative;
    font-family: "Source Sans 3", Arial, sans-serif;
    color: var(--brand-blue);
  }
  .card {
    position: absolute;
    top: 160px;
    width: 392px;
    height: 606px;
    background: var(--card-bg);
  }
  .card--front { left: 185px; }
  .card--back  { left: 631px; }

  .brand-square {
    position: absolute;
    left: 50%;
    transform: translateX(-50%);
    background: linear-gradient(135deg, var(--brand-light) 0%, var(--brand-blue) 60%, var(--brand-deep) 100%);
  }
  .card--front .brand-square { top: 56px; width: 100px; height: 100px; }
  .card--back  .brand-square { top: 121px; width: 198px; height: 198px; }

  .wordmark {
    position: absolute;
    left: 0; right: 0;
    text-align: center;
    font-family: "Cinzel", "Times New Roman", serif;
    font-weight: 700;
    text-transform: uppercase;
    color: var(--brand-blue);
    line-height: 1;
  }
  .wordmark__name { display: block; font-size: 29px; letter-spacing: 0.3px; }
  .wordmark__sub  { display: block; font-size: 19px; margin-top: 10px; font-weight: 600; letter-spacing: 0.2px; }
  .card--front .wordmark { top: 208px; }
  .card--back  .wordmark { top: 457px; }

  .rule {
    position: absolute;
    left: 37px; right: 37px;
    top: 275px;
    height: 1px;
    background: var(--rule-blue);
  }

  .person {
    position: absolute;
    top: 340px;
    left: 0; right: 0;
    text-align: center;
    font-weight: 400;
  }
  .person__name  { font-size: 22px; line-height: 30px; }
  .person__title { font-size: 18px; line-height: 24px; margin-top: 2px; }

  .contact {
    position: absolute;
    left: 45px;
    top: 480px;
    list-style: none;
    font-size: 16.5px;
    font-weight: 400;
    line-height: 21px;
  }
</style>
</head>
<body>
  <section class="card card--front">
    <div class="brand-square" aria-hidden="true"></div>
    <h1 class="wordmark">
      <span class="wordmark__name">Saltwater</span>
      <span class="wordmark__sub">General Contractors</span>
    </h1>
    <div class="rule"></div>
    <div class="person">
      <p class="person__name">Dale Brennick</p>
      <p class="person__title">Owner</p>
    </div>
    <ul class="contact">
      <li>48 Tidewater Ln Port Orchard</li>
      <li>WA 98366</li>
      <li>360-555-0142</li>
      <li>saltwatercontractors@example.com</li>
    </ul>
  </section>

  <section class="card card--back">
    <div class="brand-square" aria-hidden="true"></div>
    <h2 class="wordmark">
      <span class="wordmark__name">Saltwater</span>
      <span class="wordmark__sub">General Contractors</span>
    </h2>
  </section>
</body>
</html>
```